Bravo Ledger Path Tracker

Consumers track their three credit scores. I have sent an illustration after one update of their credit scores. Many consumers will have a dozen updates during one year. I would like to show a history of the last 24 months. Put together a design that is attractive and easy to look at and follow. I have updated some ideas for graphs (Apr 5, 2022)

Target Market(s)

Consumers tracking their credit scores

Coding

Coded - Design and coding required

Number of Pages Required

1 page

Colors
0054AA
0677BA
7BADD7
CADEEF
E8F1F8
00AB8E
00BBA5
67D7C9
C6EFE9
E9F9F6

Requirements
Must have
• Scores from 350 to 850 pon the left hand side - dates the credit scores were pulled at the bottom on the x axis
Nice to have
• 3 digit credit score for each of the three scores /

```html
<!DOCTYPE html>
<html lang="en">
<head>
<meta charset="utf-8">
<title>Bravo Ledger Path Tracker – Credit Score History</title>
<link rel="stylesheet" href="https://fonts.googleapis.com/css2?family=Poppins:wght@400;500;600;700;800&display=swap">
<style>
:root{
  --page-bg:#ffffff;
  --header-bg:#f7f7f5;
  --brand-blue:#1d5bd6;
  --brand-green:#1fbf6a;
  --title-blue:#0a14e0;
  --axis-green:#0e8a3a;
  --rule:#8a8a8a;
  --grid:#e6e6e6;
  --tick:#666666;
  --meridian:#5b7fe0;
  --crestline:#2ccf8e;
  --ardent:#f01818;
}
*{margin:0;padding:0;box-sizing:border-box}
html,body{width:1200px;height:891px;overflow:hidden;background:var(--page-bg);font-family:"Poppins",sans-serif}
.canvas{position:relative;width:1200px;height:891px;overflow:hidden}
.site-header{position:absolute;left:0;top:0;width:1200px;height:100px;background:var(--header-bg)}
.brand{position:absolute;left:89px;top:31px;display:flex;align-items:center;gap:9px}
.brand-mark{width:43px;height:38px;background:var(--brand-blue);border-radius:4px}
.brand-name{font-size:17px;font-weight:500;color:var(--brand-blue);letter-spacing:.1px}
.page-title{position:absolute;left:84px;top:158px;font-size:25px;font-weight:800;color:var(--title-blue);letter-spacing:-.2px}
.title-rule{position:absolute;left:83px;top:196px;width:1032px;height:1px;background:var(--rule)}
.score-chart{position:absolute;left:0;top:0;width:1200px;height:891px}
.tick-label{font-family:"Poppins",sans-serif;font-size:17px;fill:var(--tick)}
.legend-label{font-family:"Poppins",sans-serif;font-size:24px;fill:#6b6b6b}
.axis-title{font-family:"Poppins",sans-serif;font-size:26px;font-weight:800}
.tip-text{font-family:"Poppins",sans-serif;fill:#fff;font-size:15px}
</style>
</head>
<body>
<div class="canvas">
  <header class="site-header">
    <div class="brand">
      <span class="brand-mark"></span>
      <span class="brand-name">Bravo Ledger Path</span>
    </div>
  </header>
  <h1 class="page-title">MY CREDIT SCORE HISTORY</h1>
  <div class="title-rule"></div>

  <svg class="score-chart" viewBox="0 0 1500 1114" role="img" aria-label="Line chart of Meridian, Crestline and Ardent credit scores from January to December">
    <!-- legend -->
    <g class="legend">
      <rect x="439" y="327" width="52" height="27" fill="rgba(91,127,224,.12)" stroke="var(--meridian)" stroke-width="2"/>
      <text class="legend-label" x="503" y="348">MERIDIAN</text>
      <rect x="628" y="327" width="52" height="27" fill="rgba(44,220,160,.18)" stroke="var(--crestline)" stroke-width="2"/>
      <text class="legend-label" x="694" y="348">CRESTLINE</text>
      <rect x="870" y="327" width="52" height="27" fill="rgba(255,99,99,.2)" stroke="var(--ardent)" stroke-width="2"/>
      <text class="legend-label" x="934" y="348">ARDENT</text>
    </g>

    <!-- grid -->
    <g class="grid" stroke="var(--grid)" stroke-width="1">
      <line x1="228" y1="367" x2="1357" y2="367"/><line x1="228" y1="454" x2="1357" y2="454"/>
      <line x1="228" y1="541" x2="1357" y2="541"/><line x1="228" y1="628" x2="1357" y2="628"/>
      <line x1="228" y1="714" x2="1357" y2="714"/><line x1="228" y1="801" x2="1357" y2="801"/>
      <line x1="228" y1="888" x2="1357" y2="888"/>
      <line x1="240" y1="367" x2="240" y2="900"/><line x1="342" y1="367" x2="342" y2="900"/>
      <line x1="443" y1="367" x2="443" y2="900"/><line x1="545" y1="367" x2="545" y2="900"/>
      <line x1="647" y1="367" x2="647" y2="900"/><line x1="748" y1="367" x2="748" y2="900"/>
      <line x1="850" y1="367" x2="850" y2="900"/><line x1="951" y1="367" x2="951" y2="900"/>
      <line x1="1053" y1="367" x2="1053" y2="900"/><line x1="1155" y1="367" x2="1155" y2="900"/>
      <line x1="1256" y1="367" x2="1256" y2="900"/><line x1="1357" y1="367" x2="1357" y2="900"/>
    </g>

    <!-- y ticks -->
    <g class="y-ticks" text-anchor="end">
      <text class="tick-label" x="202" y="373">900</text><text class="tick-label" x="202" y="460">800</text>
      <text class="tick-label" x="202" y="547">700</text><text class="tick-label" x="202" y="634">600</text>
      <text class="tick-label" x="202" y="720">500</text><text class="tick-label" x="202" y="807">400</text>
      <text class="tick-label" x="202" y="894">300</text>
    </g>
    <!-- x ticks -->
    <g class="x-ticks" text-anchor="middle">
      <text class="tick-label" x="240" y="942">JAN</text><text class="tick-label" x="342" y="942">FEB</text>
      <text class="tick-label" x="443" y="942">MAR</text><text class="tick-label" x="545" y="942">APR</text>
      <text class="tick-label" x="647" y="942">MAY</text><text class="tick-label" x="748" y="942">JUN</text>
      <text class="tick-label" x="850" y="942">JUL</text><text class="tick-label" x="951" y="942">AUG</text>
      <text class="tick-label" x="1053" y="942">SEP</text><text class="tick-label" x="1155" y="942">OCT</text>
      <text class="tick-label" x="1256" y="942">NOV</text><text class="tick-label" x="1357" y="942">DEC</text>
    </g>

    <!-- Meridian -->
    <g class="series-meridian">
      <path fill="rgba(91,127,224,.1)" d="M240 844.6 C281 825.5 301 754.3 342 749.1 C383 743.9 402 860.3 443 818.6 C484 776.9 504 631.2 545 540.8 C586 450.4 606 392.8 647 366.8 C688 340.8 707 367.1 748 410.6 C789 454.1 809 549.5 850 584.2 C891 618.9 910 601.6 951 584.2 C992 566.8 1012 523.4 1053 497.4 C1094 471.4 1114 410.6 1155 454 C1196 497.4 1215 645 1256 714.4 C1297 783.8 1316 783.8 1357 801.2 L1357 888 L240 888 Z"/>
      <path fill="none" stroke="var(--meridian)" stroke-width="2.5" d="M240 844.6 C281 825.5 301 754.3 342 749.1 C383 743.9 402 860.3 443 818.6 C484 776.9 504 631.2 545 540.8 C586 450.4 606 392.8 647 366.8 C688 340.8 707 367.1 748 410.6 C789 454.1 809 549.5 850 584.2 C891 618.9 910 601.6 951 584.2 C992 566.8 1012 523.4 1053 497.4 C1094 471.4 1114 410.6 1155 454 C1196 497.4 1215 645 1256 714.4 C1297 783.8 1316 783.8 1357 801.2"/>
      <g fill="rgba(91,127,224,.15)" stroke="var(--meridian)" stroke-width="2">
        <circle cx="240" cy="844.6" r="7"/><circle cx="342" cy="749.1" r="7"/><circle cx="443" cy="818.6" r="7"/>
        <circle cx="545" cy="540.8" r="7"/><circle cx="647" cy="366.8" r="7"/><circle cx="748" cy="410.6" r="7"/>
        <circle cx="850" cy="584.2" r="7"/><circle cx="951" cy="584.2" r="7"/><circle cx="1053" cy="497.4" r="7"/>
        <circle cx="1155" cy="454" r="7"/><circle cx="1256" cy="714.4" r="7"/><circle cx="1357" cy="801.2" r="7"/>
      </g>
    </g>

    <!-- Crestline -->
    <g class="series-crestline">
      <path fill="rgba(44,220,160,.15)" d="M240 818.6 C281 801.2 301 735.3 342 731.8 C383 728.3 402 783.8 443 801.2 C484 818.6 504 870.7 545 818.6 C586 766.5 606 596.4 647 540.8 C688 485.2 707 532.1 748 540.8 C789 549.5 809 575.5 850 584.2 C891 592.9 910 601.6 951 584.2 C992 566.8 1012 523.4 1053 497.4 C1094 471.4 1114 471.4 1155 454 C1196 436.6 1215 428 1256 410.6 C1297 393.2 1316 375.6 1357 366.8 L1357 888 L240 888 Z"/>
      <path fill="none" stroke="var(--crestline)" stroke-width="2.5" d="M240 818.6 C281 801.2 301 735.3 342 731.8 C383 728.3 402 783.8 443 801.2 C484 818.6 504 870.7 545 818.6 C586 766.5 606 596.4 647 540.8 C688 485.2 707 532.1 748 540.8 C789 549.5 809 575.5 850 584.2 C891 592.9 910 601.6 951 584.2 C992 566.8 1012 523.4 1053 497.4 C1094 471.4 1114 471.4 1155 454 C1196 436.6 1215 428 1256 410.6 C1297 393.2 1316 375.6 1357 366.8"/>
      <g fill="rgba(44,220,160,.18)" stroke="var(--crestline)" stroke-width="2">
        <circle cx="240" cy="818.6" r="7"/><circle cx="342" cy="731.8" r="7"/><circle cx="443" cy="801.2" r="7"/>
        <circle cx="545" cy="818.6" r="7"/><circle cx="647" cy="540.8" r="7"/><circle cx="748" cy="540.8" r="7"/>
        <circle cx="850" cy="584.2" r="7"/><circle cx="951" cy="584.2" r="7"/><circle cx="1053" cy="497.4" r="7"/>
        <circle cx="1155" cy="454" r="7"/><circle cx="1256" cy="410.6" r="7"/><circle cx="1357" cy="366.8" r="7"/>
      </g>
    </g>

    <!-- Ardent -->
    <g class="series-ardent">
      <path fill="rgba(255,99,99,.18)" d="M240 714.4 C281 710.9 301 723 342 697 C383 671 402 580.7 443 584.2 C484 587.7 504 740.4 545 714.4 C586 688.4 606 523.5 647 454 C688 384.5 707 379 748 366.8 C789 354.6 809 306.3 850 393.2 C891 480.1 910 789 951 801.2 C992 813.4 1012 530.4 1053 454 C1094 377.6 1114 428 1155 419.3 C1196 410.6 1215 325.5 1256 410.6 C1297 495.7 1316 757.8 1357 844.6 L1357 888 L240 888 Z"/>
      <path fill="none" stroke="var(--ardent)" stroke-width="2.5" d="M240 714.4 C281 710.9 301 723 342 697 C383 671 402 580.7 443 584.2 C484 587.7 504 740.4 545 714.4 C586 688.4 606 523.5 647 454 C688 384.5 707 379 748 366.8 C789 354.6 809 306.3 850 393.2 C891 480.1 910 789 951 801.2 C992 813.4 1012 530.4 1053 454 C1094 377.6 1114 428 1155 419.3 C1196 410.6 1215 325.5 1256 410.6 C1297 495.7 1316 757.8 1357 844.6"/>
      <g fill="rgba(255,99,99,.2)" stroke="var(--ardent)" stroke-width="2">
        <circle cx="240" cy="714.4" r="7"/><circle cx="342" cy="697" r="7"/><circle cx="443" cy="584.2" r="7"/>
        <circle cx="545" cy="714.4" r="7"/><circle cx="647" cy="454" r="7"/><circle cx="748" cy="366.8" r="7"/>
        <circle cx="850" cy="393.2" r="7"/><circle cx="951" cy="801.2" r="7"/><circle cx="1053" cy="454" r="7"/>
        <circle cx="1155" cy="419.3" r="7"/><circle cx="1256" cy="410.6" r="7"/><circle cx="1357" cy="844.6" r="7"/>
      </g>
    </g>

    <!-- tooltip -->
    <g class="tooltip">
      <path d="M757 540.8 L766 533 L766 520 Q766 515 771 515 L924 515 Q929 515 929 520 L929 562 Q929 567 924 567 L771 567 Q766 567 766 562 L766 549 Z" fill="rgba(0,0,0,.82)"/>
      <text class="tip-text" x="766" y="533" font-weight="700">JUN</text>
      <rect x="765" y="544" width="14" height="14" fill="#c6f7e4" stroke="#fff" stroke-width="1"/>
      <text class="tip-text" x="783" y="556">CRESTLINE: 700</text>
    </g>

    <!-- axis titles -->
    <text class="axis-title" fill="var(--title-blue)" text-anchor="middle" transform="translate(125 642) rotate(-90)">Credit Score</text>
    <text class="axis-title" fill="var(--axis-green)" text-anchor="middle" x="742" y="1010">Credit Pull Date</text>
  </svg>
</div>
</body>
</html>
```